New Innovative Counselling and psychotherapy Service needs Business Card design

Keep it simple and professional. On one side, just company name and logo (perhaps in all blue) and maybe a tag line.

On other side (all white) my name and Qualifications in centre

Industry/Entity Type

Health And Wellness

Contact Information for Business Card

Derek Hollis
Counsellor & Psychotherapist
BSc (Psychol.), BA, Dip. (Couns. & Psych.), PG.Cert (CBT), MGVrA, NWTF

I will also require Mobile no, Email and web site address of which I'll pass on to final designer.

Font styles to use
Sans Serif

Requirements
Must have
• My Logo Only and please use the colours in logo that is in it.
Should not have
• Any other images

```html
<!DOCTYPE html>
<html lang="en">
<head>
<meta charset="utf-8">
<title>Harbor Grove – Business Card</title>
<link rel="stylesheet" href="https://fonts.googleapis.com/css2?family=Montserrat:wght@400&family=Roboto:wght@400;700&display=swap">
<style>
  :root {
    --bg: #e8e8e8;
    --card-white: #ffffff;
    --brand-blue: #49a9dd;
    --brand-blue-deep: #3d93c9;
    --brand-green: #8dc35a;
    --grad-start: #5bb8e6;
    --grad-mid: #7fcab8;
    --grad-end: #a0d56f;
    --ink: #333a40;
    --ink-soft: #4a5157;
  }
  * { box-sizing: border-box; margin: 0; padding: 0; }
  html, body {
    width: 1200px;
    height: 726px;
    overflow: hidden;
    background: var(--bg);
  }
  .canvas {
    position: relative;
    width: 1200px;
    height: 726px;
    display: flex;
    align-items: center;
    justify-content: center;
    gap: 40px;
  }
  .card {
    position: relative;
    width: 520px;
    height: 298px;
    border-radius: 3px;
    overflow: hidden;
    box-shadow: 0 6px 18px rgba(0, 0, 0, 0.14);
  }

  /* Front face */
  .card--front {
    background: linear-gradient(100deg, var(--grad-start) 0%, var(--grad-mid) 50%, var(--grad-end) 100%);
    display: flex;
    align-items: center;
    justify-content: center;
  }
  .card--front .wordmark {
    font-family: "Montserrat", sans-serif;
    font-weight: 400;
    font-size: 46px;
    letter-spacing: 0.5px;
    color: var(--card-white);
  }

  /* Back face */
  .card--back {
    background: var(--card-white);
  }
  .card--back .brand-disc {
    position: absolute;
    left: 10px;
    top: 120px;
    width: 240px;
    height: 240px;
  }
  .card--back .wordmark {
    position: absolute;
    right: 28px;
    top: 30px;
    font-family: "Montserrat", sans-serif;
    font-weight: 400;
    font-size: 31px;
    color: var(--ink);
  }
  .details {
    position: absolute;
    right: 28px;
    top: 90px;
    text-align: right;
    font-family: "Roboto", sans-serif;
    color: var(--ink-soft);
  }
  .details .person-name {
    font-weight: 700;
    font-size: 21px;
    color: var(--brand-blue);
    margin-bottom: 3px;
  }
  .details .role,
  .details .credentials {
    font-size: 11.5px;
    line-height: 1.35;
  }
  .contact {
    list-style: none;
    margin-top: 18px;
    font-size: 12.5px;
    line-height: 1.6;
  }
  .contact li {
    display: flex;
    justify-content: flex-end;
    align-items: center;
    gap: 7px;
  }
  .contact svg {
    width: 11px;
    height: 11px;
    flex: none;
  }
</style>
</head>
<body>
<main class="canvas">

  <section class="card card--front" aria-label="Business card front">
    <span class="wordmark">Harbor Grove</span>
  </section>

  <section class="card card--back" aria-label="Business card back">
    <svg class="brand-disc" viewBox="0 0 240 240" aria-hidden="true">
      <circle cx="120" cy="120" r="120" fill="var(--brand-blue)"/>
    </svg>

    <span class="wordmark">Harbor Grove</span>

    <div class="details">
      <p class="person-name">Derek Hollis</p>
      <p class="role">Counsellor &amp; Psychotherapist</p>
      <p class="credentials">BSc (Psychol.), BA, Dip. (Couns. &amp;<br>Psych.), PG.Cert (CBT), MGVrA, NWTF</p>

      <ul class="contact">
        <li>5550 123 4567
          <svg viewBox="0 0 12 12" aria-label="Phone"><path d="M1 4c0-2 2-3 5-3s5 1 5 3l-2 1-1-1H4L3 5 1 4zM3 6h6l1 5H2l1-5z" fill="var(--grad-mid)"/></svg>
        </li>
        <li>derek.h@HarborGrove.com
          <svg viewBox="0 0 12 12" aria-label="Email"><rect x="0.5" y="2.5" width="11" height="7" fill="var(--brand-green)"/><path d="M0.5 2.5 6 7l5.5-4.5" fill="none" stroke="#fff" stroke-width="1"/></svg>
        </li>
        <li>www.HarborGrove.com
          <svg viewBox="0 0 12 12" aria-label="Website"><circle cx="6" cy="6" r="5.5" fill="var(--brand-green)"/><path d="M0.5 6h11M6 0.5c-3 3-3 8 0 11M6 0.5c3 3 3 8 0 11" fill="none" stroke="#fff" stroke-width="0.8"/></svg>
        </li>
      </ul>
    </div>
  </section>

</main>
</body>
</html>
```